Bref créative
Edgy modern Letterhead an B. card for jet charter company
Veltaro Corporation
Professional
Peter Haldane
Founder, Chief Pilot
246 W. Harbor Ave., Suite 2020
Long Beach, CA 90815
855.5.VELTARO
phal@veltaro-example.com
veltaro-example.com
Use: Veltaro Corporation for company name

```html
<!DOCTYPE html>
<html lang="en">
<head>
<meta charset="utf-8">
<title>Veltaro Corporation – Stationery</title>
<link rel="stylesheet" href="https://fonts.googleapis.com/css2?family=Montserrat:wght@400;500;600&display=swap">
<style>
  :root{
    --bg:#3b3b3b;
    --paper:#ffffff;
    --ink:#2b2b2b;
    --ink-soft:#6d6d6d;
    --swoosh:#bdbdbd;
    --swoosh-dark:#8f8f8f;
    --card-black:#121212;
    --line:#9a9a9a;
  }
  html,body{margin:0;padding:0;overflow:hidden;}
  body{background:var(--bg);}
  .canvas{position:relative;width:1200px;height:754px;overflow:hidden;background:var(--bg);
    font-family:"Montserrat",sans-serif;color:var(--ink);}
  .sheet{position:absolute;background:var(--paper);overflow:hidden;}
  .swoosh{position:absolute;inset:0;width:100%;height:100%;}
  .brand{position:absolute;font-family:"Montserrat",sans-serif;font-weight:500;color:var(--ink);letter-spacing:.5px;}
  .jet-art{position:absolute;background:linear-gradient(90deg,#9c9c9c,#7a7a7a);border-radius:40% 60% 10% 10%;}
  .footer-line{position:absolute;left:0;right:0;text-align:center;font-size:5.5px;line-height:1.5;color:#f4f4f4;letter-spacing:.3px;white-space:nowrap;}

  /* Letterhead */
  .letterhead{left:50px;top:40px;width:320px;height:414px;}
  .letterhead .brand{left:34px;top:28px;font-size:20px;}
  .letter-body{position:absolute;left:34px;top:72px;width:250px;font-size:5.6px;line-height:1.55;color:var(--ink);}
  .letter-body p{margin:0 0 5px;}
  .seal{position:absolute;left:34px;top:252px;width:16px;height:16px;border-radius:50%;background:#a9d3e8;}
  .letterhead .footer-line{bottom:6px;}

  /* Fax */
  .fax{left:400px;top:40px;width:320px;height:414px;}
  .fax .brand{left:30px;top:28px;font-size:20px;}
  .fax-title{position:absolute;right:30px;top:70px;font-weight:600;font-size:14px;letter-spacing:2px;}
  .fax-table{position:absolute;left:30px;top:92px;width:260px;border-collapse:collapse;font-size:7px;}
  .fax-table td{border:1px solid var(--line);height:18px;padding:0 5px;}
  .fax-table td.label{width:46px;font-weight:600;}
  .fax-checks{position:absolute;left:30px;top:210px;display:flex;gap:16px;font-size:7px;}
  .fax-checks span::before{content:"";display:inline-block;width:7px;height:7px;border:1px solid var(--ink);margin-right:4px;vertical-align:-1px;}
  .fax .footer-line{bottom:6px;}

  /* Envelope */
  .envelope{left:750px;top:40px;width:400px;height:200px;}
  .envelope .flap{position:absolute;left:0;top:0;width:100%;height:54px;background:var(--swoosh);}
  .envelope .brand{right:30px;top:16px;font-size:18px;color:#ffffff;}
  .return-address{position:absolute;left:22px;top:66px;font-size:6px;line-height:1.5;color:var(--ink-soft);}

  /* Note card */
  .notecard{left:750px;top:272px;width:400px;height:250px;}
  .notecard .brand{left:40px;top:22px;font-size:20px;}
  .notecard .footer-line{bottom:2px;color:var(--ink-soft);}

  /* Business cards */
  .bcard{position:absolute;top:500px;width:320px;height:183px;overflow:hidden;}
  .bcard-front{left:50px;background:var(--card-black);}
  .bcard-front .brand{left:0;right:0;top:70px;text-align:center;font-size:30px;color:#ffffff;}
  .bcard-back{left:400px;background:var(--paper);}
  .bcard-back .brand{right:24px;top:68px;font-size:26px;}
  .contact{position:absolute;left:54px;top:30px;font-size:7px;line-height:1.6;}
  .contact .name{font-weight:600;font-size:9px;}
  .contact .title{color:var(--ink-soft);margin-bottom:10px;}
  .contact .row{display:flex;align-items:center;gap:5px;}
  .contact svg{width:7px;height:7px;fill:var(--ink);}
</style>
</head>
<body>
<div class="canvas">

  <!-- Letterhead -->
  <section class="sheet letterhead">
    <svg class="swoosh" viewBox="0 0 320 414" preserveAspectRatio="none" aria-hidden="true">
      <path d="M230 0 Q300 16 320 92 L320 0Z" fill="var(--swoosh)"/>
      <path d="M0 300 Q70 398 320 396 L320 414 L0 414Z" fill="var(--swoosh)"/>
      <path d="M0 340 Q90 404 320 404 L320 414 L0 414Z" fill="var(--swoosh-dark)"/>
    </svg>
    <div class="brand">veltaro</div>
    <div class="letter-body">
      <p>March 4, 2024</p>
      <p>Client Name<br>Company Address<br>City, State ZIP</p>
      <p>Dear Client,</p>
      <p>Thank you for choosing our charter service. We are pleased to confirm your upcoming flight and the details of your private itinerary.</p>
      <p>Our crew will meet you at the terminal one hour before departure. Please let us know of any special requests for catering or ground transport.</p>
      <p>We look forward to welcoming you on board.</p>
      <p>Sincerely,<br><br>Peter Haldane<br>Founder, Chief Pilot</p>
    </div>
    <div class="seal"></div>
    <div class="jet-art" role="img" aria-label="Small private jet silhouette" style="left:150px;top:372px;width:26px;height:9px;"></div>
    <div class="footer-line">246 W. Harbor Ave., Suite 2020 · Long Beach, CA 90815<br>855.5.VELTARO · veltaro-example.com</div>
  </section>

  <!-- Fax sheet -->
  <section class="sheet fax">
    <svg class="swoosh" viewBox="0 0 320 414" preserveAspectRatio="none" aria-hidden="true">
      <path d="M230 0 Q300 16 320 92 L320 0Z" fill="var(--swoosh)"/>
      <path d="M0 300 Q70 398 320 396 L320 414 L0 414Z" fill="var(--swoosh)"/>
      <path d="M0 340 Q90 404 320 404 L320 414 L0 414Z" fill="var(--swoosh-dark)"/>
    </svg>
    <div class="brand">veltaro</div>
    <div class="fax-title">FAX</div>
    <table class="fax-table">
      <tr><td class="label">To</td><td></td><td class="label">From</td><td></td></tr>
      <tr><td class="label">Fax</td><td></td><td class="label">Phone</td><td></td></tr>
      <tr><td class="label">Date</td><td></td><td class="label">Pages</td><td></td></tr>
      <tr><td class="label">Re</td><td colspan="3"></td></tr>
    </table>
    <div class="fax-checks"><span>Urgent</span><span>Review</span><span>Reply</span><span>Comments</span></div>
    <div class="jet-art" role="img" aria-label="Small private jet silhouette" style="left:150px;top:372px;width:26px;height:9px;"></div>
    <div class="footer-line">246 W. Harbor Ave., Suite 2020 · Long Beach, CA 90815<br>855.5.VELTARO · veltaro-example.com</div>
  </section>

  <!-- Envelope -->
  <section class="sheet envelope">
    <div class="flap"></div>
    <div class="brand">veltaro</div>
    <div class="return-address">Veltaro Corporation<br>246 W. Harbor Ave., Suite 2020<br>Long Beach, CA 90815</div>
  </section>

  <!-- Note card -->
  <section class="sheet notecard">
    <svg class="swoosh" viewBox="0 0 400 250" preserveAspectRatio="none" aria-hidden="true">
      <path d="M300 0 Q380 10 400 70 L400 0Z" fill="var(--swoosh)"/>
      <path d="M0 170 Q90 240 400 236 L400 250 L0 250Z" fill="var(--swoosh)"/>
      <path d="M0 205 Q110 246 400 244 L400 250 L0 250Z" fill="var(--swoosh-dark)"/>
    </svg>
    <div class="brand">veltaro</div>
    <div class="jet-art" role="img" aria-label="Small private jet silhouette" style="left:230px;top:208px;width:30px;height:10px;"></div>
    <div class="footer-line" style="bottom:14px;">855.5.VELTARO · veltaro-example.com</div>
  </section>

  <!-- Business card front -->
  <section class="bcard bcard-front">
    <div class="brand">veltaro</div>
  </section>

  <!-- Business card back -->
  <section class="bcard bcard-back">
    <svg class="swoosh" viewBox="0 0 320 183" preserveAspectRatio="none" aria-hidden="true">
      <path d="M0 0 L34 0 Q18 90 40 183 L0 183Z" fill="var(--card-black)"/>
    </svg>
    <div class="contact">
      <div class="name">Peter Haldane</div>
      <div class="title">Founder, Chief Pilot</div>
      <div class="row"><svg viewBox="0 0 10 10"><path d="M5 0a3.5 3.5 0 0 0-3.5 3.5C1.5 6 5 10 5 10s3.5-4 3.5-6.5A3.5 3.5 0 0 0 5 0zm0 5a1.5 1.5 0 1 1 0-3 1.5 1.5 0 0 1 0 3z"/></svg>246 W. Harbor Ave., Suite 2020</div>
      <div class="row" style="padding-left:12px">Long Beach, CA 90815</div>
      <div class="row"><svg viewBox="0 0 10 10"><path d="M2 0l2 2.5-1 1.2a6 6 0 0 0 3.3 3.3l1.2-1L10 8l-1.5 2C4 10 0 6 0 1.5z"/></svg>855.5.VELTARO</div>
      <div class="row"><svg viewBox="0 0 10 10"><path d="M0 2h10v6H0zM0 2l5 3.5L10 2" fill="none" stroke="#2b2b2b"/></svg>phal@veltaro-example.com</div>
      <div class="row"><svg viewBox="0 0 10 10"><circle cx="5" cy="5" r="4.3" fill="none" stroke="#2b2b2b"/></svg>veltaro-example.com</div>
    </div>
    <div class="brand">veltaro</div>
  </section>

</div>
</body>
</html>
```